Halvern Ridge Plants and Nursery needs a business street sign.

I have three businesses located at the same address: The Halvern Ridge Plants & Nursery, The Marrow Stall, and The Brackett Commons. I am looking for a 4’ x 8’ street sign to represent all three businesses as one retail experience. It needs to be eye catching yet simple enough that people can fully read it while driving by. I have logos for the greenhouse and village however I do not have anything for The Marrow Stall. I’m looking for some type of font that’s similar or in between the two attached logos for The Marrow Stall.

Requirements
Must have
• Horizontal Sign, Eye catching, yet simple design so people see it while driving by.
Nice to have
• Horizontal Sign
Should not have
• I’m open to the design being both vertical and horizontal. Please provide both options

```html
<!DOCTYPE html>
<html lang="en">
<head>
<meta charset="utf-8">
<title>Halvern Ridge Plants &amp; Nursery — Street Sign</title>
<link href="https://fonts.googleapis.com/css2?family=Outfit:wght@600;700;800&display=swap" rel="stylesheet">
<style>
  :root {
    --page-bg: #ecebe8;
    --sign-bg: #ffffff;
    --commons-red: #9c3a30;
    --nursery-green: #1b8a22;
    --maroon: #4a0d0d;
    --stall-teal: #10393b;
    --band-bg: #e2dbd5;
    --band-text: #0f3638;
    --meadow-white: #ffffff;
    --meadow-pink: #f0b9cc;
    --meadow-lilac: #b9a6dc;
    --meadow-gold: #f7c560;
    --meadow-coral: #ef8a6e;
    --meadow-stem: #9fc09a;
  }
  * { margin: 0; padding: 0; box-sizing: border-box; }
  html, body { width: 1200px; height: 1200px; overflow: hidden; }
  body {
    background: var(--page-bg);
    font-family: "Outfit", sans-serif;
    position: relative;
  }
  .street-sign {
    position: absolute;
    left: 40px;
    top: 320px;
    width: 1120px;
    height: 560px;
    background: var(--sign-bg);
    box-shadow: 0 6px 24px rgba(0,0,0,0.14);
    overflow: hidden;
  }
  .brand-row {
    position: absolute;
    left: 0; top: 0;
    width: 100%;
    height: 305px;
  }
  .brand {
    position: absolute;
    font-weight: 800;
    text-align: center;
  }
  .brand--commons {
    left: 20px; top: 108px; width: 320px;
    font-size: 44px;
    line-height: 1.0;
    color: var(--commons-red);
  }
  .brand--nursery {
    left: 350px; top: 58px; width: 520px;
    font-size: 56px;
    line-height: 1.02;
    color: var(--nursery-green);
  }
  .website {
    position: absolute;
    left: 350px; top: 238px; width: 520px;
    text-align: center;
    font-weight: 700;
    font-size: 24px;
    color: var(--maroon);
  }
  .brand--stall {
    left: 880px; top: 112px; width: 230px;
    font-size: 40px;
    line-height: 1.02;
    color: var(--stall-teal);
  }
  .services-band {
    position: absolute;
    left: 0; top: 305px;
    width: 100%;
    height: 65px;
    background: var(--band-bg);
    display: flex;
    align-items: center;
    justify-content: center;
    font-weight: 700;
    font-size: 34px;
    letter-spacing: 0.5px;
    color: var(--band-text);
  }
  .wildflower-meadow {
    position: absolute;
    left: 0; top: 370px;
    width: 100%;
    height: 190px;
    background:
      linear-gradient(to bottom, var(--meadow-white) 0%, rgba(255,255,255,0.55) 45%, rgba(255,255,255,0) 100%),
      linear-gradient(to right,
        var(--meadow-pink) 0%,
        var(--meadow-gold) 14%,
        var(--meadow-lilac) 30%,
        var(--meadow-pink) 46%,
        var(--meadow-coral) 60%,
        var(--meadow-gold) 72%,
        var(--meadow-lilac) 84%,
        var(--meadow-pink) 100%);
  }
  .wildflower-meadow::after {
    content: "";
    position: absolute;
    left: 0; bottom: 0;
    width: 100%;
    height: 40%;
    background: linear-gradient(to bottom, rgba(159,192,154,0) 0%, var(--meadow-stem) 100%);
    opacity: 0.7;
  }
</style>
</head>
<body>
  <div class="street-sign">
    <div class="brand-row">
      <div class="brand brand--commons">The Brackett<br>Commons</div>
      <div class="brand brand--nursery">The Halvern Ridge<br>Plants &amp; Nursery</div>
      <div class="website">www.halvernridgeplants.net</div>
      <div class="brand brand--stall">The Marrow<br>Stall</div>
    </div>
    <div class="services-band">LANDSCAPE, PLANNING, DESIGN, CONSTRUCTION</div>
    <div class="wildflower-meadow" role="img" aria-label="Watercolour border of colourful wildflowers in pink, purple, yellow, orange and red with green stems"></div>
  </div>
</body>
</html>
```